Brightfield Yard Service and Beyond LLC

• Mowing
• Weed eating
•Edging
• hedge trimming
• landscaping
•mulching
•yard clean up
• pressure washing

Target Market(s)

Everyone

Contact Information for Business Card

Licensed and insured

Font styles to use
Serif

Colors
59FF00
82FF00
B8FF75
E3FFCB
F4FFEA
F0912C
F2A743
F7CA91
FBE8D2
FDF5EE
EE7325
F08F49
F5BC92
FAE3D3
FDF4ED
EB3D1F
EC4F4E
F09395
F8D3D4
FCEDEE
E54698
E96AAD
F1A4CE
F9D9EA
FCEFF6

```html
<!DOCTYPE html>
<html lang="en">
<head>
<meta charset="utf-8">
<title>Brightfield Yard Service and Beyond LLC – Business Card</title>
<link rel="stylesheet" href="https://fonts.googleapis.com/css2?family=Cinzel:wght@400;700&display=swap">
<style>
  :root {
    --backdrop: #55575b;
    --leaf-green: #4aa300;
    --leaf-green-light: #6cc21a;
    --leaf-green-soft: #58b30b;
    --card-white: #ffffff;
    --badge-orange: #f0912c;
    --text-white: #ffffff;
  }
  * { box-sizing: border-box; margin: 0; padding: 0; }
  html, body {
    width: 1200px; height: 851px; overflow: hidden;
    background: var(--backdrop);
  }
  .canvas {
    position: relative; width: 1200px; height: 851px;
    display: flex; align-items: center; justify-content: center; gap: 40px;
  }
  .card {
    position: relative; width: 540px; height: 309px;
    border-radius: 22px; overflow: hidden;
    box-shadow: 0 14px 30px rgba(0,0,0,.35);
  }

  /* Back side */
  .card-back { background: var(--leaf-green); }
  .card-back .tool-pattern {
    position: absolute; inset: 0;
    background:
      radial-gradient(ellipse at 25% 30%, var(--leaf-green-light) 0%, transparent 55%),
      radial-gradient(ellipse at 80% 75%, var(--leaf-green-soft) 0%, transparent 60%),
      var(--leaf-green);
  }
  .service-list {
    position: absolute; inset: 0;
    display: flex; flex-direction: column; align-items: center; justify-content: center;
    gap: 4px;
    font-family: "Cinzel", serif; font-weight: 700;
    color: var(--text-white); font-size: 18px; letter-spacing: .3px; text-align: center;
    text-transform: uppercase;
  }

  /* Front side */
  .card-front { background: var(--card-white); }
  .front-swoosh { position: absolute; inset: 0; }
  .brand {
    position: absolute; left: 52px; top: 34px; right: 24px;
    font-family: "Cinzel", serif; font-weight: 700; color: var(--leaf-green);
  }
  .brand-name {
    display: flex; align-items: center; gap: 12px;
    font-size: 46px; line-height: 1;
  }
  .brand-dot {
    width: 30px; height: 30px; border-radius: 50%; background: var(--leaf-green); flex: none;
  }
  .brand-tagline {
    display: flex; align-items: center; gap: 10px;
    margin-top: 6px; padding-left: 4px; font-size: 20px;
  }
  .brand-tagline .rule { width: 30px; height: 2px; background: var(--leaf-green); }
  .license-badge {
    display: inline-block; margin-top: 8px; margin-left: 80px;
    background: var(--badge-orange); color: var(--text-white);
    font-family: "Cinzel", serif; font-weight: 700; font-size: 15px;
    padding: 4px 16px; border-radius: 16px;
  }
  .phone {
    position: absolute; right: 46px; bottom: 28px;
    display: flex; align-items: center; gap: 10px;
    font-family: "Cinzel", serif; font-weight: 400; font-size: 38px;
    color: var(--text-white);
  }
  .phone svg { width: 28px; height: 28px; }
</style>
</head>
<body>
<main class="canvas">

  <section class="card card-back" aria-label="Card back: services">
    <div class="tool-pattern" role="img" aria-label="Light green line pattern of garden tools: rakes, wheelbarrows, watering cans, buckets and planters"></div>
    <div class="service-list">
      <p>Mowing | Weed Eating | Edging</p>
      <p>Hedge Trimming | Landscaping | Mulching</p>
      <p>Yard Clean Up | Pressure Washing</p>
    </div>
  </section>

  <section class="card card-front" aria-label="Card front: name and contact">
    <svg class="front-swoosh" viewBox="0 0 540 309" preserveAspectRatio="none" aria-hidden="true">
      <path class="green-base" d="M0 250 Q330 225 540 110 L540 309 L0 309 Z" fill="var(--leaf-green)"/>
      <path class="thin-swoosh" d="M140 215 Q400 195 520 70 Q400 205 140 215 Z" fill="var(--leaf-green)"/>
    </svg>

    <div class="brand">
      <div class="brand-name"><span class="brand-dot"></span>BRIGHTFIELD</div>
      <div class="brand-tagline"><span class="rule"></span>Yard Service &amp; Beyond LLC<span class="rule"></span></div>
      <span class="license-badge">LICENSED AND INSURED</span>
    </div>

    <div class="phone">
      <svg viewBox="0 0 24 24" aria-hidden="true">
        <path fill="var(--text-white)" d="M6.6 10.8a15.1 15.1 0 0 0 6.6 6.6l2.2-2.2a1 1 0 0 1 1-.25 11.4 11.4 0 0 0 3.6.57 1 1 0 0 1 1 1V20a1 1 0 0 1-1 1A17 17 0 0 1 3 4a1 1 0 0 1 1-1h3.5a1 1 0 0 1 1 1c0 1.25.2 2.45.57 3.57a1 1 0 0 1-.25 1z"/>
      </svg>
      <span>555-014-2290</span>
    </div>
  </section>

</main>
</body>
</html>
```